2022 Grenache Hillside Vineyard Sketch Wine Label

Size:4"X4"
Wine: 2022 Grenache
Vineyard Name: Oak Ledge Vineyard
AVA: Solano County
Alcohol by Volume:15%
Volume:750ml
Must Feature a hillside vineyard on the label somehow, I picture it being a sketch but it doesn't have to be. Not looking for anything flashy or colorful but maybe a pop of color somewhere. I am not yet sure that I want to include our name, but you can try to work in "MFX" somewhere on the label if it fits the design.
The Label must include all the information listed above. The Grenache was grown in a hillside vineyard, so I wanted the label to prominently feature a hillside vineyard. You can layout the label however you see best, but the vintage and varietal should be prominent, the ABV can be in small type face but must be legible following WLQ guidelines. If you are able to make the vineyard name pop as well that would be good.
You don't have to use these, but our standard fonts we use are:
For Varietal: Bianca
Secondary (vintage, AVA, Vineyard):Helvetica
ABV/Volume: PT Serif
Thank you, look forward to the results

```html
<!DOCTYPE html>
<html lang="en">
<head>
<meta charset="utf-8">
<title>Oak Ledge Vineyard – 2022 Grenache Label</title>
<link rel="stylesheet" href="https://fonts.googleapis.com/css2?family=Arimo:wght@400;700&family=PT+Serif:wght@400&display=swap">
<style>
  :root {
    --page-bg: #f3f3f1;
    --label-paper: #f7f7f2;
    --label-edge: #e4e4dc;
    --sage: #6d7d55;
    --sage-light: #b9c3a4;
    --sage-pale: #dfe4d3;
    --ink: #141414;
  }
  html, body {
    margin: 0;
    padding: 0;
    width: 1200px;
    height: 2811px;
    overflow: hidden;
    background: var(--page-bg);
  }
  .canvas {
    position: relative;
    width: 1200px;
    height: 2811px;
  }
  .wine-label {
    position: absolute;
    left: 100px;
    top: 905px;
    width: 1000px;
    height: 1000px;
    background: radial-gradient(ellipse at center, #fbfbf8 0%, var(--label-paper) 70%, #efefe8 100%);
    border-radius: 30px;
    box-shadow: 0 6px 18px rgba(0,0,0,0.12);
  }
  .vineyard-scene {
    position: absolute;
    left: 131px;
    top: 74px;
    width: 736px;
    height: 446px;
    border-radius: 50% / 46%;
    background: radial-gradient(ellipse at 50% 55%, var(--sage-light) 0%, var(--sage-pale) 60%, rgba(223,228,211,0) 100%);
  }
  .abv-seal {
    position: absolute;
    left: 736px;
    top: 401px;
    width: 122px;
    height: 122px;
  }
  .label-text {
    position: absolute;
    left: 0;
    width: 100%;
    margin: 0;
    text-align: center;
    line-height: 1;
  }
  .vineyard-name {
    top: 592px;
    font-family: "Arimo", Helvetica, sans-serif;
    font-weight: 700;
    font-size: 50px;
    letter-spacing: 0.14em;
    color: var(--sage);
  }
  .ava {
    top: 672px;
    font-family: "Arimo", Helvetica, sans-serif;
    font-weight: 700;
    font-size: 37px;
    letter-spacing: 0.16em;
    color: var(--ink);
  }
  .vintage {
    top: 741px;
    font-family: "Arimo", Helvetica, sans-serif;
    font-weight: 700;
    font-size: 37px;
    letter-spacing: 0.16em;
    color: var(--sage);
  }
  .varietal {
    top: 783px;
    font-family: "Arimo", Helvetica, sans-serif;
    font-weight: 700;
    font-size: 40px;
    letter-spacing: 0.16em;
    color: var(--sage);
  }
  .volume-abv {
    top: 871px;
    font-family: "PT Serif", Georgia, serif;
    font-size: 38px;
    color: var(--ink);
  }
</style>
</head>
<body>
  <main class="canvas">
    <section class="wine-label">
      <div class="vineyard-scene" role="img" aria-label="Sketched hillside vineyard with rows of vines, cypress trees, a farmhouse and a mountain under clouds"></div>
      <svg class="abv-seal" viewBox="0 0 122 122" aria-hidden="true">
        <circle cx="61" cy="61" r="58" fill="#ffffff" stroke="var(--ink)" stroke-width="3"/>
        <circle cx="61" cy="61" r="50" fill="none" stroke="var(--ink)" stroke-width="2"/>
      </svg>
      <h1 class="label-text vineyard-name">OAK LEDGE VINEYARD</h1>
      <p class="label-text ava">SOLANO COUNTY</p>
      <p class="label-text vintage">2022</p>
      <p class="label-text varietal">GRENACHE</p>
      <p class="label-text volume-abv">750ML / ACL. 15% VOL</p>
    </section>
  </main>
</body>
</html>
```